A website design for a consultation firm

We are located in Istanbul, Turkey and offers our consultation services to customers interested in investing in Realestate, Education and Investment particularly this coming from Arab world and English speaking countries.

The site should carry our message of deep knowledge about the Turkish markets in the mentioned sectors of interest, sincerity and keenness.

The final deliverable of the winning design should include:
- The source files of the final designs. e.g. AI, PSD ..etc
- The redline markup for the design using a Specctr or any other similar tool.

Target Market(s)

English and Arabic speaking countries with a Turkish theme since we are a Turkish company

Industry/Entity Type

Consulting

Number of Pages Required

2 page

Font styles to use
Sans Serif

Requirements
Must have
• The site should serve the following main sections:
• - Why QVD?
• - Reports & studies
• - Sectors
• - Our team
• - Contact
• We need a design that could be converted into a WordPress theme.
• The design should be in English but should accommodate other languages including RTL.
• You can use the color theme you like as long as it does't dissolve the logo.
• The site should link into our accounts on the following networks:
• - Twitter
• - Facebook
• - LinkedIn
• The design should be responsive and nicely rendered on Desktop, Tablets and Smart phones.
Nice to have
• The site would be nice to balance between being informative and

```html
<!DOCTYPE html>
<html lang="en">
<head>
<meta charset="utf-8">
<title>QVD Consulting</title>
<link href="https://fonts.googleapis.com/css2?family=Raleway:wght@500;600;700&family=Lato:wght@400;700&display=swap" rel="stylesheet">
<style>
:root{
  --navy:#1f3461;
  --navy-deep:#1b2d55;
  --red:#e11b2b;
  --red-dark:#c0121f;
  --ink:#222;
  --muted:#555;
  --paper:#f3f3f3;
  --wood:#2b2b2b;
  --white:#fff;
}
*{box-sizing:border-box;margin:0;padding:0}
html,body{width:1200px;height:2773px;overflow:hidden}
body{position:relative;font-family:'Lato',sans-serif;color:var(--ink);background:var(--white)}
.abs{position:absolute}
h2,h3,.brand,.hero-title{font-family:'Raleway',sans-serif}

/* header */
.site-header{position:absolute;top:0;left:0;width:1200px;height:120px;z-index:3;border-top:3px solid var(--red)}
.brand{position:absolute;left:100px;top:22px;display:flex;align-items:center;gap:10px;font-size:40px;font-weight:700;color:var(--red)}
.brand-dot{width:22px;height:22px;border-radius:50%;background:var(--navy)}
.lang{position:absolute;left:595px;top:12px;font-size:14px;color:var(--navy);font-family:'Lato',serif}
.lang span{margin:0 4px}
.lang .on{color:var(--navy);font-weight:700}
.lang .off{color:var(--red)}
.top-mail{position:absolute;left:724px;top:4px;height:30px;display:flex;align-items:center;gap:8px;font-size:13px;color:var(--navy)}
.top-phone{position:absolute;left:925px;top:0;width:170px;height:38px;background:var(--red);border-radius:0 0 22px 22px;display:flex;align-items:center;justify-content:center;gap:10px;color:#fff;font-size:17px;font-weight:700}
.main-nav{position:absolute;top:70px;left:0;font-size:14.5px;color:#222}
.main-nav a{position:absolute;white-space:nowrap;text-decoration:none;color:#222}
.main-nav a.current{color:var(--red)}
.main-nav .sep{position:absolute;top:4px;width:1px;height:12px;background:#bbb}

/* hero */
.hero{position:absolute;left:0;top:0;width:1200px;height:640px;background:linear-gradient(180deg,#fff 0%,#f1f1f1 45%,#e6e6e6 100%)}
.hero-scene{position:absolute;left:0;top:120px;width:1200px;height:520px;background:radial-gradient(ellipse at 790px 220px,#d21b22 0%,#b01218 8%,rgba(176,18,24,0) 14%),linear-gradient(180deg,#f6f6f6,#e9e9e9)}
.hero-title{position:absolute;left:100px;top:426px;font-size:29.5px;font-weight:600;line-height:42px;color:#1a1a1a}
.btn-start{position:absolute;left:100px;top:532px;width:166px;height:37px;border-radius:20px;background:var(--navy);color:#fff;font-size:16px;font-weight:700;display:flex;align-items:center;padding-left:14px;text-transform:uppercase}
.btn-start .go{position:absolute;right:4px;top:4px;width:29px;height:29px;border-radius:50%;background:var(--red);display:flex;align-items:center;justify-content:center}

.notch{position:absolute;width:0;height:0;border-left:20px solid transparent;border-right:20px solid transparent;z-index:2}

/* section titles */
.section-title{position:absolute;left:0;width:1200px;text-align:center;font-size:35px;font-weight:600}
.title-rule{position:absolute;height:1px}
.title-rule::after{content:"";position:absolute;top:-20px;width:1px;height:41px;background:inherit}
.title-rule.l::after{right:0}
.title-rule.r::after{left:0}

/* welcome */
.welcome{position:absolute;left:0;top:640px;width:1200px;height:340px;background:var(--paper)}
.welcome p{position:absolute;left:111px;top:144px;width:980px;text-align:center;font-size:12.6px;line-height:24px;color:#333}
.btn-more{position:absolute;left:532px;top:264px;width:136px;height:32px;display:flex;border-radius:3px;overflow:hidden;font-size:14px;font-weight:700;color:#fff}
.btn-more .lbl{flex:1;background:var(--red);display:flex;align-items:center;justify-content:center}
.btn-more .go{width:30px;background:var(--navy);display:flex;align-items:center;justify-content:center}

/* services */
.services{position:absolute;left:0;top:980px;width:1200px;height:570px;background:linear-gradient(180deg,#262626,#333 50%,#262626)}
.service-card{position:absolute;top:150px;width:313px;height:368px;background:#fff;box-shadow:0 2px 6px rgba(0,0,0,.4)}
.service-card .pic{position:absolute;left:15px;top:20px;width:283px;height:170px}
.service-card h3{position:absolute;top:222px;width:100%;text-align:center;color:var(--navy);font-size:23px;font-weight:700}
.service-card p{position:absolute;left:25px;top:260px;width:263px;text-align:center;font-size:12.6px;line-height:20px;color:#333}
.plus{position:absolute;left:141px;top:342px;width:31px;height:26px;background:var(--red);color:#fff;font-size:20px;font-weight:700;display:flex;align-items:center;justify-content:center}

/* team */
.team{position:absolute;left:0;top:1550px;width:1200px;height:573px;background:var(--paper)}
.member{position:absolute;top:166px;width:282px;height:340px;background:#fff;border:2px solid #e2e2e2}
.member .pic{position:absolute;left:16px;top:16px;width:246px;height:164px}
.member h3{position:absolute;top:196px;width:100%;text-align:center;color:var(--red);font-size:18.5px;font-weight:700}
.member .role{position:absolute;top:228px;width:100%;text-align:center;color:var(--navy);font-size:14.5px;font-weight:700}
.member p{position:absolute;left:22px;top:254px;width:234px;text-align:center;font-size:13px;line-height:20px;color:#222}
.arrow{position:absolute;top:332px}

/* contact */
.contact{position:absolute;left:0;top:2123px;width:1200px;height:493px;background:var(--navy)}
.contact .lead{position:absolute;top:125px;width:100%;text-align:center;color:#fff;font-size:16.5px}
.col-head{position:absolute;top:192px;color:#fff;font-family:'Lato',sans-serif;font-size:20px;font-weight:700}
.field{position:absolute;left:126px;width:257px;height:29px;background:#fff;border-radius:2px;font-size:12px;color:#555;padding:7px 10px}
.btn-send{position:absolute;left:126px;top:420px;width:95px;height:30px;background:var(--red);color:#fff;font-size:13px;font-weight:700;display:flex;align-items:center;justify-content:center;letter-spacing:1px}
.map{position:absolute;left:440px;top:234px;width:344px;height:176px;background:linear-gradient(135deg,#c9dbe9 0%,#e8e1cf 35%,#ead9cc 60%,#c6d9e8 100%)}
.info{position:absolute;left:832px;color:#fff;font-size:13.5px;line-height:19px;display:flex;gap:14px}
.info svg{flex:none;margin-top:2px}

/* newsletter */
.newsletter{position:absolute;left:0;top:2616px;width:1200px;height:106px;background:var(--red)}
.nl-icon{position:absolute;left:122px;top:30px;width:52px;height:52px;border:2px solid #fff;border-radius:50%;display:flex;align-items:center;justify-content:center}
.nl-title{position:absolute;left:188px;top:35px;color:#fff;font-family:'Raleway',sans-serif;font-size:27px;font-weight:600}
.nl-input{position:absolute;left:501px;top:35px;width:367px;height:38px;background:#fff;font-size:12.5px;color:#333;padding:11px 12px}
.nl-btn{position:absolute;left:883px;top:35px;width:188px;height:38px;background:var(--navy);color:#fff;font-size:18px;font-weight:700;display:flex;align-items:center;justify-content:center;letter-spacing:.5px}

.site-footer{position:absolute;left:0;top:2722px;width:1200px;height:51px;background:var(--navy-deep);color:#fff;font-size:12.5px;display:flex;align-items:center;justify-content:center}
</style>
</head>
<body>

<section class="hero">
  <div class="hero-scene" role="img" aria-label="White chess pawns in a row with a tall red king piece standing out on a white reflective surface"></div>
  <h1 class="hero-title">Looking To Minimize The New Market<br>Entrance Risk?&nbsp; Your Search Is Over</h1>
  <div class="btn-start">Get Started
    <span class="go"><svg width="14" height="12" viewBox="0 0 14 12"><path d="M1 1l5 5-5 5M7 1l5 5-5 5" fill="none" stroke="#fff" stroke-width="2.2"/></svg></span>
  </div>
</section>

<header class="site-header">
  <div class="brand"><span class="brand-dot"></span>QVD Consulting</div>
  <div class="lang"><span class="on">EN</span>|<span class="off">TR</span>|<span class="off">AR</span> ▾</div>
  <div class="top-mail">
    <svg width="22" height="22" viewBox="0 0 22 22"><circle cx="11" cy="11" r="10" fill="var(--navy)"/><rect x="6" y="7.5" width="10" height="7" fill="#fff"/><path d="M6 7.5l5 4 5-4" fill="none" stroke="var(--navy)" stroke-width="1.2"/></svg>
    inquiry@qvdconsulting.com
  </div>
  <div class="top-phone">
    <svg width="22" height="22" viewBox="0 0 22 22"><circle cx="11" cy="11" r="10" fill="none" stroke="#fff" stroke-width="1.6"/><path d="M8 6.5l2 2-1 1.5c.6 1.4 1.6 2.4 3 3l1.5-1 2 2-1.5 1.5c-3.5-.3-6.7-3.5-7-7z" fill="#fff"/></svg>
    123 456 7890
  </div>
  <nav class="main-nav">
    <a class="current" style="left:327px">Home</a>
    <span class="sep" style="left:383px"></span>
    <a style="left:406px">Why Choose Us?</a>
    <span class="sep" style="left:536px"></span>
    <a style="left:558px">Reports &amp; studies</a>
    <span class="sep" style="left:694px"></span>
    <a style="left:715px">Our Works</a>
    <span class="sep" style="left:806px"></span>
    <a style="left:828px">Sectors</a>
    <span class="sep" style="left:898px"></span>
    <a style="left:920px">Our team</a>
    <span class="sep" style="left:1000px"></span>
    <a style="left:1023px">Contact Us</a>
  </nav>
</header>

<div class="notch" style="left:580px;top:640px;border-top:16px solid var(--navy)"></div>

<section class="welcome">
  <span class="title-rule l" style="left:216px;top:88px;width:130px;background:var(--red)"></span>
  <h2 class="section-title" style="top:66px;color:var(--navy)">Welcome To QVD Consulting</h2>
  <span class="title-rule r" style="left:854px;top:88px;width:130px;background:var(--red)"></span>
  <p>Lorem ipsum dolor sit amet, consectetuer adipiscing elit, sed diam nonummy nibh euismod tincidunt ut laoreet dolore magna aliquam erat volutpat. Ut wisi enim ad minim veniam, quis nostrud exerci tation ullamcorper suscipit lobortis nisl ut aliquip ex ea commodo consequat. Duis autem vel eum iriure dolor in hendrerit in vulputate velit esse molestie consequat, vel illum dolore eu feugiat nulla facilisis at vero eros et accumsan et iusto odio dignissim qui blandit praesent luptatum zzril delenit augue duis dolore te feugait nulla facilisi .....</p>
  <div class="btn-more"><span class="lbl">Read More</span><span class="go"><svg width="14" height="12" viewBox="0 0 14 12"><path d="M1 1l5 5-5 5M7 1l5 5-5 5" fill="none" stroke="#fff" stroke-width="2.2"/></svg></span></div>
</section>

<div class="notch" style="left:572px;top:980px;border-left-width:28px;border-right-width:28px;border-top:28px solid var(--red)"></div>

<section class="services">
  <span class="title-rule l" style="left:340px;top:90px;width:130px;background:var(--red)"></span>
  <h2 class="section-title" style="top:68px;color:#fff">Our Services</h2>
  <span class="title-rule r" style="left:732px;top:90px;width:130px;background:var(--red)"></span>

  <article class="service-card" style="left:98px">
    <div class="pic" role="img" aria-label="Illuminated Istanbul mosque with minarets at dusk" style="background:linear-gradient(180deg,#3a63b8 0%,#5f7fc4 50%,#2a3a5e 80%,#1d2a3e 100%)"></div>
    <h3>Real Estate</h3>
    <p>Lorem ipsum dolor sit amet, consectetuer adipiscing elit, sed diam nonummy eternibh euismod tincidunt ut laoreet do</p>
    <span class="plus">+</span>
  </article>
  <article class="service-card" style="left:444px">
    <div class="pic" role="img" aria-label="Smiling student holding books in a campus hallway" style="background:linear-gradient(90deg,#9a5b3a 0%,#d9b99a 35%,#e7c4b0 55%,#c47a5a 100%)"></div>
    <h3>Education</h3>
    <p>Lorem ipsum dolor sit amet, consectetuer adipiscing elit, sed diam nonummy eternibh euismod tincidunt ut laoreet do</p>
    <span class="plus">+</span>
  </article>
  <article class="service-card" style="left:788px">
    <div class="pic" role="img" aria-label="Hand holding a glowing glass sphere with a rising chart inside" style="background:radial-gradient(circle at 55% 40%,#f4c36a 0%,#a86a2a 30%,#2a1a10 70%,#120c08 100%)"></div>
    <h3>Investments</h3>
    <p>Lorem ipsum dolor sit amet, consectetuer adipiscing elit, sed diam nonummy eternibh euismod tincidunt ut laoreet do</p>
    <span class="plus">+</span>
  </article>
</section>

<div class="notch" style="left:572px;top:1550px;border-left-width:28px;border-right-width:28px;border-top:28px solid #262626"></div>

<section class="team">
  <span class="title-rule l" style="left:356px;top:95px;width:130px;background:var(--red)"></span>
  <h2 class="section-title" style="top:73px;color:var(--navy)">Our Team</h2>
  <span class="title-rule r" style="left:714px;top:95px;width:130px;background:var(--red)"></span>

  <svg class="arrow" style="left:72px" width="22" height="44" viewBox="0 0 22 44"><path d="M20 2L3 22l17 20" fill="none" stroke="#c8c8c8" stroke-width="2"/></svg>
  <svg class="arrow" style="left:1104px" width="22" height="44" viewBox="0 0 22 44"><path d="M2 2l17 20L2 42" fill="none" stroke="#c8c8c8" stroke-width="2"/></svg>

  <article class="member" style="left:124px">
    <div class="pic" role="img" aria-label="Portrait of a team member in a dark suit" style="background:linear-gradient(180deg,#e3e3e3 0%,#bdbdbd 55%,#2f3340 100%)"></div>
    <h3>Person Name</h3><div class="role">Account Manager</div>
    <p>Lorem ipsum dolor sit amet, consectetuer adipiscing elit, sed diam nonummy nibh euismod tincidu</p>
  </article>
  <article class="member" style="left:459px">
    <div class="pic" role="img" aria-label="Portrait of a senior team member" style="background:linear-gradient(180deg,#f1f1f1 0%,#e2cbb8 50%,#5a5d66 100%)"></div>
    <h3>Person Name</h3><div class="role">Account Manager</div>
    <p>Lorem ipsum dolor sit amet, consectetuer adipiscing elit, sed diam nonummy nibh euismod tincidu</p>
  </article>
  <article class="member" style="left:793px">
    <div class="pic" role="img" aria-label="Portrait of a team member in a light blouse" style="background:linear-gradient(180deg,#ececec 0%,#e0c294 45%,#f2ece6 100%)"></div>
    <h3>Person Name</h3><div class="role">Account Manager</div>
    <p>Lorem ipsum dolor sit amet, consectetuer adipiscing elit, sed diam nonummy nibh euismod tincidu</p>
  </article>
</section>

<div class="notch" style="left:580px;top:2123px;border-top:20px solid var(--red)"></div>

<section class="contact">
  <span class="title-rule l" style="left:356px;top:83px;width:130px;background:var(--red)"></span>
  <h2 class="section-title" style="top:61px;color:#fff">Contact Us</h2>
  <span class="title-rule r" style="left:714px;top:83px;width:130px;background:var(--red)"></span>
  <p class="lead">Come on by! We'd love to see you</p>

  <h3 class="col-head" style="left:126px">Quick Inquiry</h3>
  <h3 class="col-head" style="left:440px">Location Map</h3>
  <h3 class="col-head" style="left:835px">Contact Us</h3>

  <div class="field" style="top:236px">Name</div>
  <div class="field" style="top:272px">Email</div>
  <div class="field" style="top:308px">Subject</div>
  <div class="field" style="top:344px;height:64px">Message</div>
  <div class="btn-send">SEND</div>

  <div class="map" role="img" aria-label="Map of Turkey and surrounding region"></div>

  <div class="info" style="top:232px">
    <svg width="12" height="16" viewBox="0 0 12 16"><path d="M6 1a5 5 0 0 0-5 5c0 4 5 9 5 9s5-5 5-9a5 5 0 0 0-5-5z" fill="#fff"/><circle cx="6" cy="6" r="2" fill="var(--navy)"/></svg>
    <div><b>QVD Consulting</b><br><span style="font-size:12.5px">Harlow Ltd, Meridian Court, Elm Row<br>Square, London EC2 4PA.</span></div>
  </div>
  <div class="info" style="top:322px">
    <svg width="12" height="14" viewBox="0 0 12 14"><path d="M1 1l3 0 1 3-1.5 1.5c.8 2 2 3.2 4 4L9 8l3 1v3c-6 0-11-5-11-11z" fill="#fff"/></svg>
    <b>(123) 456 7890</b>
  </div>
  <div class="info" style="top:351px">
    <svg width="12" height="14" viewBox="0 0 12 14"><rect x="1" y="5" width="10" height="8" rx="1" fill="#fff"/><rect x="3" y="1" width="6" height="4" fill="#fff"/></svg>
    <b>(123) 456 7890</b>
  </div>
  <div class="info" style="top:380px">
    <svg width="13" height="12" viewBox="0 0 13 12"><rect x="0.5" y="2" width="12" height="8" fill="#fff"/><path d="M.5 2l6 4.5 6-4.5" fill="none" stroke="var(--navy)" stroke-width="1"/></svg>
    <span>inquiry@qvdconsulting.com</span>
  </div>
</section>

<section class="newsletter">
  <div class="nl-icon"><svg width="26" height="20" viewBox="0 0 26 20"><rect x="1" y="2" width="24" height="16" fill="#fff"/><path d="M1 2l12 9 12-9" fill="none" stroke="var(--red)" stroke-width="1.8"/></svg></div>
  <h2 class="nl-title">Sign Up For Newsletter</h2>
  <div class="nl-input">Enter your email here</div>
  <div class="nl-btn">SUBSCRIBE</div>
</section>

<footer class="site-footer">Copyright © 2016&nbsp; QvdConsulting.&nbsp; All Right Reserved</footer>

</body>
</html>
```